Landscape Construction and Design Company

We are a landscape construction and design company from New Jersey. We design and install landscapes and hardscapes for residential properties. The name of the company is Brevin's Landscape and Design LLC. We specialize mostly in planting trees and stone work, some water features. We would like to see design themes that include a tree or trees and a stone walkway or wall. We like earth tone colors. We like traditional to modern designs.

Target Market(s)

Homeowners

Industry/Entity Type

Landscape

Contact Information for Business Card

Nature themed design, earth tone colors, space for company name, address, phone numbers, email and website address

Logo Text

No text

Font styles to use
Serif

Colors

Designer to choose colors to be used in the design.

Requirements
Must have
• A tree or trees, similar to the ones uploaded in my supporting images
Nice to have
• I like trees similar to those in my uploaded supporting images. I like artistic, nature theme, earth tone colors
Should not have
• Pictures of real landscapes, cartoon looking logo or objects

```html
<!DOCTYPE html>
<html lang="en">
<head>
<meta charset="UTF-8">
<title>Brevin's Landscape and Design LLC — Business Card</title>
<link rel="stylesheet" href="https://fonts.googleapis.com/css2?family=Cinzel:wght@400;600&family=Lato:wght@400;700&display=swap">
<style>
  :root {
    --backdrop: #3a302b;
    --card-white: #f7f7f5;
    --card-green: #63a23f;
    --leaf-green: #5fa12f;
    --ink: #2b2b2b;
    --divider: #d4d4d0;
    --on-green: #ffffff;
  }
  * { margin: 0; padding: 0; box-sizing: border-box; }
  html, body { width: 1200px; height: 900px; overflow: hidden; }
  body {
    background: var(--backdrop);
    position: relative;
    font-family: "Lato", Arial, sans-serif;
  }
  .card {
    position: absolute;
    top: 300px;
    width: 525px;
    height: 300px;
    box-shadow: 0 14px 30px rgba(0,0,0,0.45);
  }
  .card--front { left: 50px; background: var(--card-white); }
  .card--back { left: 625px; background: var(--card-green); }

  .brand {
    position: absolute;
    left: 0; top: 0;
    width: 262px; height: 300px;
    display: flex;
    flex-direction: column;
    align-items: center;
    justify-content: center;
    gap: 16px;
  }
  .brand__mark {
    width: 22px; height: 22px;
    border-radius: 50%;
    background: var(--leaf-green);
  }
  .brand__name {
    font-family: "Cinzel", Georgia, serif;
    font-weight: 600;
    color: var(--leaf-green);
    text-align: center;
    font-size: 25px;
    line-height: 1.25;
  }
  .brand__name small { display: block; font-size: 13px; letter-spacing: 0.5px; }

  .divider {
    position: absolute;
    left: 262px; top: 40px;
    width: 1px; height: 220px;
    background: var(--divider);
  }

  .contact {
    position: absolute;
    left: 285px; top: 52px;
    color: var(--ink);
  }
  .contact__name {
    font-family: "Cinzel", Georgia, serif;
    font-weight: 600;
    color: var(--leaf-green);
    font-size: 20px;
  }
  .contact__title { font-size: 15px; margin-bottom: 10px; }
  .contact__list { list-style: none; font-size: 15px; line-height: 1.45; }
  .contact__list li { display: flex; align-items: center; gap: 7px; }
  .contact__list svg { width: 11px; height: 11px; flex: none; }
  .contact__address { font-size: 15px; line-height: 1.4; margin-top: 12px; }

  .back__brand {
    position: absolute;
    left: 0; right: 0; top: 95px;
    display: flex;
    flex-direction: column;
    align-items: center;
    gap: 12px;
  }
  .back__mark { width: 30px; height: 30px; border-radius: 50%; background: var(--on-green); }
  .back__name {
    font-family: "Cinzel", Georgia, serif;
    font-weight: 600;
    color: var(--on-green);
    font-size: 24px;
  }
  .back__services {
    position: absolute;
    left: 0; right: 0; bottom: 40px;
    text-align: center;
    color: var(--on-green);
    font-size: 15px;
    letter-spacing: 0.3px;
  }
</style>
</head>
<body>
  <section class="card card--front">
    <div class="brand">
      <span class="brand__mark"></span>
      <p class="brand__name">Brevin's<small>Landscape and Design LLC</small></p>
    </div>
    <span class="divider"></span>
    <div class="contact">
      <p class="contact__name">DANIEL PORTER</p>
      <p class="contact__title">Managing Director</p>
      <ul class="contact__list">
        <li><svg viewBox="0 0 12 12"><path d="M3 1l2 2.5-1.2 1.3a7 7 0 003.4 3.4L8.5 7 11 9l-1.2 2C5 11 1 7 1 2.2z" fill="#5fa12f"/></svg>444 555 7712</li>
        <li><svg viewBox="0 0 12 12"><rect x="0.5" y="2" width="11" height="8" fill="#5fa12f"/><path d="M0.5 2l5.5 4.5L11.5 2" stroke="#fff" fill="none"/></svg>info@brevinslandscape.com</li>
        <li><svg viewBox="0 0 12 12"><circle cx="6" cy="6" r="5.5" fill="#5fa12f"/></svg>www.brevinslandscape.com</li>
      </ul>
      <p class="contact__address">421, Address line here,<br>Country Name,45452</p>
    </div>
  </section>

  <section class="card card--back">
    <div class="back__brand">
      <span class="back__mark"></span>
      <p class="back__name">Brevin's</p>
    </div>
    <p class="back__services">PLANTING TREES | STONE WORK | WATER FEATURES</p>
  </section>
</body>
</html>
```